Commercial Construction Company

We need a business card design based on our current logo. We are a commercial general contractor based in Southern California that specializes in bank remodels. We would like to see designs that incorporate dark blue. The final design should portray an image of professionalism and quality.

If possible, I would like to add metallic foil to the design. Thank you

```html
<!DOCTYPE html>
<html lang="en">
<head>
<meta charset="utf-8">
<title>Halden Commercial Builders – Business Card</title>
<link href="https://fonts.googleapis.com/css2?family=Bebas+Neue&family=Montserrat:wght@400;500;600&family=Oswald:wght@600&display=swap" rel="stylesheet">
<style>
  :root {
    --bg: #2a2d33;
    --navy: #0f4a8a;
    --navy-deep: #0b3c73;
    --silver-light: #f4f4f4;
    --silver-mid: #dcdcdc;
    --silver-dark: #c4c4c4;
    --ink: #141414;
    --text-grey: #3a3a3a;
  }
  * { margin: 0; padding: 0; box-sizing: border-box; }
  html, body { width: 1200px; height: 900px; overflow: hidden; }
  body {
    background: var(--bg);
    display: flex;
    flex-direction: column;
    align-items: center;
    justify-content: center;
    gap: 40px;
  }
  .card {
    position: relative;
    width: 700px;
    height: 400px;
    overflow: hidden;
    background:
      repeating-linear-gradient(0deg, rgba(255,255,255,0.18) 0 1px, rgba(0,0,0,0.03) 1px 3px),
      linear-gradient(115deg, var(--silver-dark) 0%, var(--silver-light) 35%, var(--silver-mid) 60%, var(--silver-light) 80%, var(--silver-dark) 100%);
    box-shadow: 0 10px 30px rgba(0,0,0,0.45);
  }
  .card__accent { position: absolute; inset: 0; width: 100%; height: 100%; }

  .brand {
    position: absolute;
    display: flex;
    align-items: center;
    gap: 16px;
  }
  .brand__dot {
    width: 22px; height: 22px;
    border-radius: 50%;
    background: var(--navy);
    flex: none;
  }
  .brand__name {
    font-family: 'Oswald', sans-serif;
    font-weight: 600;
    color: var(--ink);
    text-transform: uppercase;
    line-height: 1.05;
    letter-spacing: 1px;
  }

  /* Front */
  .card--front .brand { left: 50%; top: 50%; transform: translate(-50%, -50%); }
  .card--front .brand__name { font-size: 40px; }

  /* Back */
  .card--back .brand { right: 70px; top: 150px; }
  .card--back .brand__name { font-size: 30px; }

  .person { position: absolute; left: 48px; top: 38px; }
  .person__name {
    font-family: 'Bebas Neue', sans-serif;
    font-size: 40px;
    color: var(--navy);
    letter-spacing: 1px;
    line-height: 1;
  }
  .person__title {
    font-family: 'Montserrat', sans-serif;
    font-size: 15px;
    font-weight: 500;
    color: var(--navy);
    padding-bottom: 6px;
    border-bottom: 2px solid var(--navy);
    width: 150px;
  }
  .contacts {
    position: absolute;
    left: 48px;
    top: 150px;
    list-style: none;
    display: flex;
    flex-direction: column;
    gap: 16px;
  }
  .contacts__item {
    display: flex;
    align-items: center;
    gap: 14px;
    font-family: 'Montserrat', sans-serif;
    font-size: 14px;
    color: var(--text-grey);
  }
  .contacts__icon { width: 22px; height: 22px; flex: none; }
</style>
</head>
<body>

  <!-- Front of card -->
  <section class="card card--front">
    <svg class="card__accent" viewBox="0 0 700 400" aria-hidden="true">
      <polygon points="0,0 130,0 124,6 0,6" fill="var(--navy)"/>
      <polygon points="0,0 6,0 6,60 0,66" fill="var(--navy)"/>
      <polygon points="700,400 560,400 566,394 700,394" fill="var(--navy)"/>
      <polygon points="700,400 694,400 694,330 700,324" fill="var(--navy)"/>
    </svg>
    <div class="brand">
      <span class="brand__dot"></span>
      <span class="brand__name">Halden<br>Commercial Builders</span>
    </div>
  </section>

  <!-- Back of card -->
  <section class="card card--back">
    <svg class="card__accent" viewBox="0 0 700 400" aria-hidden="true">
      <polygon points="0,0 180,0 174,6 0,6" fill="var(--navy)"/>
      <polygon points="0,0 6,0 6,70 0,76" fill="var(--navy)"/>
      <path d="M430,400 C520,360 600,300 640,200 C660,150 690,120 700,110 L700,400 Z" fill="var(--navy-deep)"/>
      <path d="M430,400 C520,360 600,300 640,200 C660,150 690,120 700,110" fill="none" stroke="#ffffff" stroke-opacity="0.6" stroke-width="3"/>
    </svg>

    <div class="person">
      <h1 class="person__name">Daniel Harlow</h1>
      <p class="person__title">President and CEO</p>
    </div>

    <ul class="contacts">
      <li class="contacts__item">
        <svg class="contacts__icon" viewBox="0 0 22 22" aria-hidden="true">
          <circle cx="11" cy="11" r="11" fill="var(--navy)"/>
          <path d="M8 6.5 L9.6 6.5 L10.4 9 L9.3 9.9 Q10.3 12 12.1 12.9 L13 11.8 L15.5 12.6 L15.5 14.2 Q15.3 15.5 13.8 15.4 Q8.5 14.7 6.7 8.3 Q6.6 6.7 8 6.5 Z" fill="#fff"/>
        </svg>
        <span>012 555 0148 , 012 555 0192</span>
      </li>
      <li class="contacts__item">
        <svg class="contacts__icon" viewBox="0 0 22 22" aria-hidden="true">
          <circle cx="11" cy="11" r="11" fill="var(--navy)"/>
          <rect x="5.5" y="7" width="11" height="8" rx="1" fill="#fff"/>
          <path d="M5.8 7.4 L11 11.4 L16.2 7.4" fill="none" stroke="var(--navy)" stroke-width="1.2"/>
        </svg>
        <span>haldenbuilders@mail.com</span>
      </li>
      <li class="contacts__item">
        <svg class="contacts__icon" viewBox="0 0 22 22" aria-hidden="true">
          <circle cx="11" cy="11" r="11" fill="var(--navy)"/>
          <circle cx="11" cy="11" r="5.5" fill="none" stroke="#fff" stroke-width="1.2"/>
          <ellipse cx="11" cy="11" rx="2.3" ry="5.5" fill="none" stroke="#fff" stroke-width="1"/>
          <line x1="5.5" y1="11" x2="16.5" y2="11" stroke="#fff" stroke-width="1"/>
        </svg>
        <span>www.haldencommercialbuilders.com</span>
      </li>
    </ul>

    <div class="brand">
      <span class="brand__dot"></span>
      <span class="brand__name">Halden<br>Commercial Builders</span>
    </div>
  </section>

</body>
</html>
```